Classic Minimalistic Business Card

Design a classic, minimalistic Business Card. Please find inspiration in the attached Classic Minimalistic examples. My information:
Name: Glen Ovamir
Company: Ovamir Capital
Logo: OC
Address: 1470 N Thornwick Rd, Suite 210 | Fenmoor, WI 53099
Phone: 555-555-0192
Email: glenovamir@pvt.insure
Slogan: Building Strength Through Capital

Feel free to leave out any of the information above except my name.

I have selected Double-sided, but I am also open to Single-sided

Target Market(s)

22-70. income greater than 150k/year

Industry/Entity Type

Finance

Contact Information for Business Card

See Project Description

Requirements
Must have
• Ivory or "antiqued" background similar to the reference pictures

```html
<!DOCTYPE html>
<html lang="en">
<head>
<meta charset="utf-8">
<title>Ovamir Capital – Business Card</title>
<link rel="stylesheet" href="https://fonts.googleapis.com/css2?family=Arvo:wght@400;700&display=swap">
<style>
  :root {
    --page: #efefef;
    --card: #8a7054;
    --band: #8f7659;
    --ink: #3b3024;
    --ink-soft: #45392b;
  }
  html, body {
    margin: 0;
    padding: 0;
    width: 1200px;
    height: 798px;
    overflow: hidden;
    background: var(--page);
    font-family: "Arvo", serif;
    color: var(--ink);
  }
  .canvas {
    position: relative;
    width: 1200px;
    height: 798px;
  }
  .card {
    position: absolute;
    width: 388px;
    height: 215px;
    background: var(--card);
  }
  .card--back { left: 521px; top: 380px; }
  .card--front { left: 314px; top: 223px; }

  .brand {
    position: absolute;
    left: 218px;
    top: 67px;
    width: 160px;
    text-align: center;
    font-size: 14.5px;
    letter-spacing: 0.08em;
    white-space: nowrap;
    color: var(--ink-soft);
  }
  .holder-name {
    position: absolute;
    left: 20px;
    top: 112px;
    margin: 0;
    font-size: 19px;
    font-weight: 400;
    letter-spacing: 0.02em;
    white-space: nowrap;
  }
  .contact, .address {
    position: absolute;
    top: 149px;
    font-size: 10.5px;
    line-height: 14px;
    white-space: nowrap;
    color: var(--ink-soft);
  }
  .contact { left: 20px; }
  .address { right: 20px; text-align: right; }
  .tagline-band {
    position: absolute;
    left: 0;
    top: 186px;
    width: 100%;
    height: 22px;
    background: var(--band);
    font-size: 11.5px;
    line-height: 22px;
    text-align: center;
    white-space: nowrap;
  }

  .brand--large {
    position: absolute;
    left: 0;
    top: 122px;
    width: 100%;
    text-align: center;
    font-size: 26px;
    letter-spacing: 0.08em;
    white-space: nowrap;
    color: var(--ink-soft);
  }
</style>
</head>
<body>
<main class="canvas">
  <section class="card card--back" aria-label="Card back">
    <div class="brand--large">Ovamir Capital</div>
  </section>

  <section class="card card--front" aria-label="Card front">
    <div class="brand">Ovamir Capital</div>
    <h1 class="holder-name">Glen Ovamir</h1>
    <div class="contact">
      555-555-0192<br>
      glenovamir@pvt.insure
    </div>
    <div class="address">
      1470 N Thornwick Rd<br>
      Suite 210 | Fenmoor, WI 53099
    </div>
    <div class="tagline-band">Building Strength Through Capital</div>
  </section>
</main>
</body>
</html>
```